training slide

We have an existing PPT template.

I am just looking for someone to make the attached slides better looking. If that goes well we have a whole bunch of presentations that need formatting in a similar style. Our customer base is made up of pharmaceutical and healthcare companies. we charge high end consultancy prices and it is very important our production value reflects this level of quality. We are not attached to the current PPT template and if anyone wants to re-visit that we would be very keen to see any ideas. We do however like our kelOrvanta logo but you can lose the energy, experience etc.

Industry/Entity Type

Training

```html
<!DOCTYPE html>
<html lang="en">
<head>
<meta charset="utf-8">
<title>Values – kelOrvanta</title>
<link rel="stylesheet" href="https://fonts.googleapis.com/css2?family=PT+Sans:wght@400;700&family=Open+Sans:wght@400;700&display=swap">
<style>
  :root {
    --bg-core: #0b7199;
    --bg-mid: #07496a;
    --bg-edge: #041d2e;
    --title-top: #d6ea7c;
    --title-bottom: #86ae2c;
    --white: #ffffff;
    --ink: #161616;
    --card-light: #f1f1f1;
    --card-light-2: #dcdcdc;
    --card-dark: #b9b9b9;
    --card-dark-2: #a3a3a3;
    --card-edge: #2a2a2a;
    --blue-top: #8fd3f6;
    --blue-bottom: #1c8ed6;
    --green-top: #b8e8a0;
    --green-bottom: #3ba62f;
    --lime-top: #cfe36e;
    --lime-bottom: #8db12a;
    --accent-blue: #2a8fd0;
    --accent-teal: #3fb8b0;
  }
  * { margin: 0; padding: 0; box-sizing: border-box; }
  html, body { width: 1200px; height: 900px; overflow: hidden; }
  body { font-family: "PT Sans", sans-serif; }

  .slide {
    position: relative;
    width: 1200px;
    height: 900px;
    overflow: hidden;
    background: radial-gradient(ellipse 720px 620px at 600px 330px, var(--bg-core) 0%, var(--bg-mid) 55%, var(--bg-edge) 100%);
  }

  .slide-title {
    position: absolute;
    left: 40px;
    top: 40px;
    font-weight: 700;
    font-size: 74px;
    line-height: 1;
    letter-spacing: 1px;
    background: linear-gradient(var(--title-top), var(--title-bottom));
    -webkit-background-clip: text;
    background-clip: text;
    color: transparent;
  }
  .slide-title-reflection {
    position: absolute;
    left: 40px;
    top: 88px;
    height: 74px;
    font-weight: 700;
    font-size: 74px;
    line-height: 1;
    letter-spacing: 1px;
    color: var(--title-bottom);
    transform: scaleY(-1);
    opacity: 0.4;
    -webkit-mask-image: linear-gradient(to top, rgba(0,0,0,0.9), transparent 45%);
    mask-image: linear-gradient(to top, rgba(0,0,0,0.9), transparent 45%);
    overflow: hidden;
  }

  .brand {
    position: absolute;
    right: 30px;
    top: 66px;
    font-weight: 400;
    font-size: 34px;
    line-height: 1;
    color: var(--white);
  }

  .edge-accent {
    position: absolute;
    top: 262px;
    height: 72px;
    background: linear-gradient(var(--accent-blue), var(--accent-teal) 60%, var(--accent-blue));
  }
  .edge-accent.left { left: 0; width: 20px; }
  .edge-accent.right { right: 0; width: 76px; }

  .value { position: absolute; }
  .value-header { position: absolute; left: 0; top: 0; }
  .value-header svg { display: block; }
  .value-label {
    position: absolute;
    inset: 0;
    display: flex;
    align-items: center;
    justify-content: center;
    color: var(--white);
    font-size: 48px;
    text-shadow: 0 2px 3px rgba(0,0,0,0.45);
  }
  .value-list {
    position: absolute;
    list-style: none;
    border: 2px solid var(--card-edge);
    background: linear-gradient(var(--card-light) 0%, var(--card-light-2) 49%, var(--card-dark) 49%, var(--card-dark-2) 100%);
    padding: 16px 0 0 12px;
    color: var(--ink);
    font-size: 35px;
    line-height: 52px;
    white-space: nowrap;
  }
  .value-list li::before { content: "•"; margin-right: 6px; }

  .value.energy { left: 50px; top: 260px; }
  .value.energy .value-list { left: 20px; top: 80px; width: 290px; height: 240px; }

  .value.credibility { left: 380px; top: 390px; }
  .value.credibility .value-list { left: 26px; top: 80px; width: 324px; height: 240px; }

  .value.relationships { left: 750px; top: 510px; }
  .value.relationships .value-list { left: 22px; top: 80px; width: 398px; height: 190px; }

  .footer {
    position: absolute;
    top: 866px;
    font-family: "Open Sans", sans-serif;
    font-size: 15px;
    color: var(--white);
  }
  .footer.copyright { left: 72px; font-weight: 700; }
  .footer.website { left: 936px; }
</style>
</head>
<body>
<main class="slide">
  <h1 class="slide-title">Values</h1>
  <div class="slide-title-reflection" aria-hidden="true">Values</div>

  <div class="brand">kelOrvanta</div>

  <div class="edge-accent left" role="img" aria-label="Decorative edge accent band"></div>
  <div class="edge-accent right" role="img" aria-label="Decorative edge accent band"></div>

  <section class="value energy">
    <div class="value-header">
      <svg width="310" height="80" viewBox="0 0 310 80" aria-hidden="true">
        <defs>
          <linearGradient id="grad-blue" x1="0" y1="0" x2="0" y2="1">
            <stop offset="0" stop-color="var(--blue-top)"/>
            <stop offset="0.45" stop-color="#45aee8"/>
            <stop offset="1" stop-color="var(--blue-bottom)"/>
          </linearGradient>
        </defs>
        <polygon points="0,0 288,0 310,22 310,78 22,78 0,58" fill="url(#grad-blue)"/>
      </svg>
      <div class="value-label">Energy</div>
    </div>
    <ul class="value-list">
      <li>Intensity</li>
      <li>Fun</li>
      <li>Determination</li>
      <li>Fortitude</li>
    </ul>
  </section>

  <section class="value credibility">
    <div class="value-header">
      <svg width="350" height="80" viewBox="0 0 350 80" aria-hidden="true">
        <defs>
          <linearGradient id="grad-green" x1="0" y1="0" x2="0" y2="1">
            <stop offset="0" stop-color="var(--green-top)"/>
            <stop offset="0.45" stop-color="#6cc453"/>
            <stop offset="1" stop-color="var(--green-bottom)"/>
          </linearGradient>
        </defs>
        <polygon points="0,0 328,0 350,22 350,78 24,78 0,58" fill="url(#grad-green)"/>
      </svg>
      <div class="value-label">Credibility</div>
    </div>
    <ul class="value-list">
      <li>Expertise</li>
      <li>Experience</li>
      <li>Professional</li>
      <li>Constant learning</li>
    </ul>
  </section>

  <section class="value relationships">
    <div class="value-header">
      <svg width="420" height="80" viewBox="0 0 420 80" aria-hidden="true">
        <defs>
          <linearGradient id="grad-lime" x1="0" y1="0" x2="0" y2="1">
            <stop offset="0" stop-color="var(--lime-top)"/>
            <stop offset="0.45" stop-color="#acc944"/>
            <stop offset="1" stop-color="var(--lime-bottom)"/>
          </linearGradient>
        </defs>
        <polygon points="0,0 398,0 420,22 420,78 22,78 0,58" fill="url(#grad-lime)"/>
      </svg>
      <div class="value-label">Relationships</div>
    </div>
    <ul class="value-list">
      <li>Networking</li>
      <li>Trust</li>
      <li>Influencing at the top</li>
    </ul>
  </section>

  <p class="footer copyright">© kelOrvanta Ltd. 2013 All Rights Reserved</p>
  <p class="footer website">www.kelOrvanta.co.uk</p>
</main>
</body>
</html>
```